Online business manager needs a website

I need a website designed and then coded. I am an online business manager serving a number of different industries providing administrative support to existing small businesses and helping solo practitioners get their new business up and running.

I didn't have a logo formally designed but have been using the attached avatar and wouldn't mind something that incorporated that.

The business doesn't have an official name, so I've just been using my name Lena Pruvost, Online Business Manager or Lena Pruvost, OBM. I've attached two documents that I have made previously for an example of content.

I would prefer the final site be in Wordpress.

Requirements
Must have
• A way to contact me, testimonials, list of services

```html
<!DOCTYPE html>
<html lang="en">
<head>
<meta charset="utf-8">
<title>Lena Pruvost – Online Business Manager</title>
<link href="https://fonts.googleapis.com/css2?family=Montserrat:wght@300;400;500;600;700&family=PT+Serif:wght@400;700&display=swap" rel="stylesheet">
<style>
:root{
  --navy:#050a2e;
  --navy2:#0d1a5c;
  --blue:#2f7bf0;
  --green:#157a56;
  --cyan:#2ec8e6;
  --ink:#111;
  --body:#333;
  --soft:#eef5fc;
  --line:#dde3ec;
}
*{box-sizing:border-box;margin:0;padding:0}
html,body{width:1200px;height:4051px;overflow:hidden;background:#fff}
body{font-family:'Montserrat',sans-serif;color:var(--body)}
.page{position:relative;width:1200px;height:4051px;overflow:hidden}
.abs{position:absolute}
.serif{font-family:'PT Serif',serif;font-weight:700;color:var(--ink)}
.accent{color:var(--blue)}
.spark{position:absolute;width:26px;height:22px}

/* hero */
.hero{position:absolute;left:0;top:0;width:1200px;height:580px}
.brand{left:157px;top:18px;display:flex;align-items:center;gap:8px}
.brand-mark{width:56px;height:46px;border-radius:4px;background:linear-gradient(135deg,#f2c55a,#3aa37a)}
.brand-name{color:var(--cyan);font-weight:700;font-size:18px;letter-spacing:1px;line-height:1}
.brand-sub{color:#fff;font-size:12px;margin-top:4px}
.nav{left:543px;top:31px;display:flex;gap:31px;font-size:13px;color:#fff}
.nav .on{color:var(--cyan)}
.nav-btn{left:917px;top:22px;width:121px;height:36px;border:1.5px solid var(--cyan);border-radius:18px;color:#fff;font-size:13px;display:flex;align-items:center;justify-content:center}
.hero-first{left:157px;top:148px;color:#fff;font-size:76px;font-weight:300;line-height:1}
.hero-last{left:157px;top:222px;color:#fff;font-size:76px;font-weight:700;line-height:1;letter-spacing:-1px}
.hero-tag{left:160px;top:327px;width:315px;height:33px;background:linear-gradient(90deg,#2e6cf0,#3ad6e8);color:#fff;font-size:14px;letter-spacing:3px;display:flex;align-items:center;justify-content:center}
.hero-copy{left:160px;top:380px;width:385px;color:#fff;font-size:12.5px;line-height:24px}
.hero-photo{left:629px;top:102px;width:410px;height:410px;border-radius:50%;background:radial-gradient(circle at 50% 40%,#d9b79a,#8a7565 60%,#6a6a72);border:4px solid #2c3f9a}
.hero-ring{left:614px;top:87px;width:440px;height:440px;border-radius:50%;border:2px solid #2ec8e6}

/* about */
.ph{border-radius:8px;border:5px solid #fff;box-shadow:0 6px 20px rgba(0,0,0,.12)}
.about-title{left:602px;top:715px;font-size:34px}
.about-copy{left:602px;top:768px;width:505px;font-size:11.5px;line-height:23px;text-align:justify;color:#222}
.about-copy p+p{margin-top:8px}

/* services */
.services{left:0;top:1137px;width:1200px;height:900px;background:var(--soft)}
.sec-title{left:0;width:1200px;text-align:center;font-size:34px}
.sec-sub{left:250px;top:1262px;width:700px;text-align:center;font-size:12px;line-height:21px;color:#222}
.card{position:absolute;width:244px;height:225px;background:#fff;border-radius:10px;box-shadow:0 4px 14px rgba(30,60,120,.12);text-align:center}
.card h3{font-family:'PT Serif',serif;font-size:16px;color:var(--ink);margin-top:73px}
.card p{font-size:10.5px;line-height:19px;padding:0 14px;margin-top:12px;color:#333}
.icon{position:absolute;width:86px;height:86px;border-radius:50%;border:4px solid #fff;box-shadow:0 3px 10px rgba(0,0,0,.15);display:flex;align-items:center;justify-content:center}
.ic-blue{background:var(--blue)}.ic-green{background:var(--green)}
.btn{position:absolute;color:#fff;font-size:12px;font-weight:600;letter-spacing:.5px;border-radius:4px;display:flex;align-items:center;justify-content:center}

/* industry */
.logo-box{position:absolute;top:2163px;width:148px;height:97px;background:#fff;box-shadow:0 3px 12px rgba(0,0,0,.1);display:flex;align-items:center;justify-content:center;text-align:center;font-weight:700;font-size:15px;color:#1d3a7a;padding:0 10px}
.arrow{position:absolute;width:28px;height:28px;border-radius:50%;display:flex;align-items:center;justify-content:center;font-size:14px}

/* testimonials */
.testi{left:0;top:2328px;width:1200px;height:472px;background:var(--soft)}
.tcard{position:absolute;top:2457px;width:446px;height:183px;background:#fff;box-shadow:0 4px 14px rgba(0,0,0,.08);text-align:center}
.stars{color:#f5b400;font-size:14px;letter-spacing:2px;margin-top:22px}
.tcard p{font-size:10.5px;line-height:19px;font-style:italic;padding:0 30px;margin-top:8px;color:#333}
.avatar{position:absolute;width:62px;height:62px;border-radius:50%;background:radial-gradient(circle,#c99a7a,#6b4a3a);border:3px solid #fff}
.tname{position:absolute;width:446px;text-align:center;font-family:'PT Serif',serif;font-weight:700;font-size:16px;color:var(--ink)}
.trole{position:absolute;width:446px;text-align:center;font-family:'PT Serif',serif;font-size:11px;color:var(--blue)}

/* rates */
.rate{position:absolute;top:2929px;width:244px;height:285px;background:#fff;border-radius:8px;box-shadow:0 4px 14px rgba(0,0,0,.1);text-align:center;overflow:hidden}
.rate-head{height:54px;color:#fff;font-family:'PT Serif',serif;font-weight:700;font-size:18px;display:flex;align-items:center;justify-content:center}
.rate-price{font-family:'PT Serif',serif;font-weight:700;font-size:34px;color:var(--ink);margin-top:18px}
.rate-note{font-size:12.5px;line-height:25px;margin-top:8px;color:#333;padding:0 16px}
.rate-small{font-size:10px;font-style:italic;margin-top:2px;color:#444}

/* contact */
.contact{left:93px;top:3288px;width:1014px;height:495px;border-radius:24px;background:linear-gradient(180deg,#f3f8ff,#e3eefc);}
.field{position:absolute;height:35px;border:1px solid #c9d4e4;border-radius:4px;background:#fff;font-size:10px;color:#555;padding:10px 8px}
.laptop{left:650px;top:3358px;width:420px;height:354px;border-radius:14px;background:linear-gradient(180deg,#9fb7c8,#e4c4a5 55%,#8f8f94)}

/* footer */
.f-title{font-family:'PT Serif',serif;font-weight:700;font-size:19px}
.f-icon{position:absolute;width:26px;height:26px;border-radius:50%;background:var(--blue);display:flex;align-items:center;justify-content:center}
.f-label{position:absolute;font-family:'PT Serif',serif;font-size:11.5px;color:#111;line-height:19px}
.f-label b{font-weight:700}
</style>
</head>
<body>
<div class="page">

  <!-- HERO -->
  <svg class="hero" viewBox="0 0 1200 580" role="img" aria-label="Night sky hero background">
    <defs>
      <radialGradient id="sky" cx="55%" cy="30%" r="80%">
        <stop offset="0" stop-color="#1b2a7a"/><stop offset=".6" stop-color="#0a1150"/><stop offset="1" stop-color="#030726"/>
      </radialGradient>
    </defs>
    <path d="M0 0H1200V503Q600 650 0 503Z" fill="url(#sky)"/>
  </svg>
  <div class="abs brand">
    <div class="brand-mark" role="img" aria-label="Avatar brand mark"></div>
    <div><div class="brand-name">LENA PRUVOST</div><div class="brand-sub">Online Business Manager</div></div>
  </div>
  <div class="abs nav"><span class="on">Home</span><span>About Me</span><span>What I Do Best</span><span>Client Love</span></div>
  <div class="abs nav-btn">Contact Me</div>
  <div class="abs hero-first">LENA</div>
  <div class="abs hero-last">PRUVOST</div>
  <div class="abs hero-tag">DIGITAL BUSINESS MANAGER</div>
  <div class="abs hero-copy">Focused on the live event and entertainment industry. Helping artists and owners to better manage their career and business by strategically reviewing systems, recommending operational efficiencies, and managing inboxes.</div>
  <div class="abs hero-ring"></div>
  <div class="abs hero-photo" role="img" aria-label="Portrait photo of Lena Pruvost"></div>

  <!-- ABOUT -->
  <div class="abs" style="left:40px;top:700px;width:300px;height:300px;border-radius:50%;background:radial-gradient(circle,#dfe8ff,rgba(255,255,255,0))"></div>
  <div class="abs ph" style="left:283px;top:668px;width:280px;height:221px;background:linear-gradient(135deg,#c9b9a8,#5a6170)" role="img" aria-label="Team meeting photo"></div>
  <div class="abs ph" style="left:77px;top:783px;width:282px;height:239px;background:linear-gradient(135deg,#e8eef4,#2a3142)" role="img" aria-label="Business team portrait photo"></div>
  <div class="abs ph" style="left:377px;top:904px;width:166px;height:162px;background:linear-gradient(180deg,#f4d07a,#4fa07c 60%,#8d8d92)" role="img" aria-label="Avatar illustration at a laptop"></div>
  <div class="abs serif about-title">About <span class="accent">Lena Pruvost</span></div>
  <svg class="spark" style="left:872px;top:705px" viewBox="0 0 26 22"><path d="M4 2l3 9M14 0l-5 12M24 8l-13 5" stroke="#111" stroke-width="2" fill="none"/></svg>
  <div class="abs about-copy">
    <p>It is a long established fact that a reader will be distracted by the readable content of a page when looking at its layout. The point of using Lorem Ipsum is that it has a more-or-less normal distribution of letters, as opposed to using 'Content here, content here', making it look like readable English. Many desktop publishing packages and web page editors now use Lorem Ipsum as their default model text, and a search for 'lorem ipsum' will uncover many web sites still in their infancy.</p>
    <p>There are many variations of passages of Lorem Ipsum available, but the majority have suffered alteration in some form, by injected humour, or randomised words which don't look even slightly believable. If you are going to use a passage of Lorem Ipsum, you need to be sure there isn't anything embarrassing hidden in the middle of text.</p>
  </div>

  <!-- SERVICES -->
  <div class="abs services"></div>
  <div class="abs serif sec-title" style="top:1196px"><span class="accent">Lena Pruvost</span> Services</div>
  <svg class="spark" style="left:745px;top:1188px" viewBox="0 0 26 22"><path d="M4 2l3 9M14 0l-5 12M24 8l-13 5" stroke="var(--blue)" stroke-width="2" fill="none"/></svg>
  <div class="abs sec-sub">There are many variations of passages of Lorem Ipsum available, but the majority have suffered alteration in some form, by injected humour, or randomised words which don't look even slightly believable</div>

  <div class="card" style="left:93px;top:1379px"><h3>Content Repurposing</h3><p>It is a long established fact that a reader will be distracted by the readable content of a page when looking at its layout. The point of using Lorem Ipsum is that it has a more-or-less normal.</p></div>
  <div class="card" style="left:349px;top:1379px"><h3>Financial Analytics</h3><p>It is a long established fact that a reader will be distracted by the readable content of a page when looking at its layout. The point of using Lorem Ipsum is that it has a more-or-less normal.</p></div>
  <div class="card" style="left:606px;top:1379px"><h3>Data Entry</h3><p>It is a long established fact that a reader will be distracted by the readable content of a page when looking at its layout. The point of using Lorem Ipsum is that it has a more-or-less normal.</p></div>
  <div class="card" style="left:863px;top:1379px"><h3>Graphic Creations</h3><p>It is a long established fact that a reader will be distracted by the readable content of a page when looking at its layout. The point of using Lorem Ipsum is that it has a more-or-less normal.</p></div>
  <div class="card" style="left:93px;top:1675px"><h3>Email Management</h3><p>It is a long established fact that a reader will be distracted by the readable content of a page when looking at its layout. The point of using Lorem Ipsum is that it has a more-or-less normal.</p></div>
  <div class="card" style="left:349px;top:1675px"><h3>Project Management</h3><p>It is a long established fact that a reader will be distracted by the readable content of a page when looking at its layout. The point of using Lorem Ipsum is that it has a more-or-less normal.</p></div>
  <div class="card" style="left:606px;top:1675px"><h3>Bookkeeping</h3><p>It is a long established fact that a reader will be distracted by the readable content of a page when looking at its layout. The point of using Lorem Ipsum is that it has a more-or-less normal.</p></div>
  <div class="card" style="left:863px;top:1675px"><h3>More Awesomeness</h3><p>It is a long established fact that a reader will be distracted by the readable content of a page when looking at its layout. The point of using Lorem Ipsum is that it has a more-or-less normal.</p></div>

  <div class="icon ic-blue" style="left:172px;top:1335px"><svg width="42" height="42" viewBox="0 0 42 42" fill="none" stroke="#fff" stroke-width="2"><circle cx="21" cy="21" r="15"/><path d="M12 17a10 10 0 0 1 16-4M30 25a10 10 0 0 1-16 4"/></svg></div>
  <div class="icon ic-green" style="left:428px;top:1335px"><svg width="42" height="42" viewBox="0 0 42 42" fill="none" stroke="#fff" stroke-width="2"><path d="M8 34h26M12 32V22M19 32V17M26 32V12M8 20l10-8 6 4 10-9"/></svg></div>
  <div class="icon ic-blue" style="left:685px;top:1335px"><svg width="42" height="42" viewBox="0 0 42 42" fill="none" stroke="#fff" stroke-width="2"><rect x="9" y="7" width="24" height="28" rx="2"/><path d="M14 14h14M14 20h14M14 26h8"/></svg></div>
  <div class="icon ic-green" style="left:942px;top:1335px"><svg width="42" height="42" viewBox="0 0 42 42" fill="none" stroke="#fff" stroke-width="2"><rect x="7" y="7" width="9" height="9"/><rect x="26" y="7" width="9" height="9"/><path d="M16 11h10M11 16v14l8 4M30 16l-8 16"/></svg></div>
  <div class="icon ic-green" style="left:172px;top:1630px"><svg width="42" height="42" viewBox="0 0 42 42" fill="none" stroke="#fff" stroke-width="2"><path d="M7 17v18h28V17L21 7Z"/><path d="M7 17l14 10 14-10M12 14v-4h18v4"/></svg></div>
  <div class="icon ic-blue" style="left:428px;top:1630px"><svg width="42" height="42" viewBox="0 0 42 42" fill="none" stroke="#fff" stroke-width="2"><circle cx="17" cy="14" r="6"/><path d="M6 34c0-8 5-12 11-12s11 4 11 12"/><circle cx="31" cy="27" r="5"/></svg></div>
  <div class="icon ic-green" style="left:685px;top:1630px"><svg width="42" height="42" viewBox="0 0 42 42" fill="none" stroke="#fff" stroke-width="2"><rect x="10" y="6" width="22" height="30" rx="2"/><rect x="14" y="10" width="14" height="7"/><path d="M15 22h2M20 22h2M25 22h2M15 27h2M20 27h2M25 27h2M15 31h2M20 31h2M25 31h2"/></svg></div>
  <div class="icon ic-blue" style="left:942px;top:1630px"><svg width="42" height="42" viewBox="0 0 42 42" fill="none" stroke="#fff" stroke-width="2"><path d="M10 20h5v14h-5zM15 21l6-11c2 0 3 2 3 4l-1 5h8c2 0 3 2 2 4l-3 9c-1 1-2 2-3 2H15"/><path d="M28 6l1 3 3 1-3 1-1 3-1-3-3-1 3-1z"/></svg></div>

  <div class="btn" style="left:550px;top:1931px;width:126px;height:33px;background:var(--blue)">CONTACT US</div>

  <!-- INDUSTRY -->
  <div class="abs serif sec-title" style="top:2096px">Industry <span class="accent">Lena Pruvost</span> Serve</div>
  <svg class="spark" style="left:752px;top:2086px" viewBox="0 0 26 22"><path d="M4 2l3 9M14 0l-5 12M24 8l-13 5" stroke="#111" stroke-width="2" fill="none"/></svg>
  <div class="arrow" style="left:43px;top:2197px;border:1px solid #ccd;color:#889">‹</div>
  <div class="logo-box" style="left:93px">Harbor Drilling</div>
  <div class="logo-box" style="left:267px">Kestrel Energy</div>
  <div class="logo-box" style="left:441px">Amberline Hotels</div>
  <div class="logo-box" style="left:615px">Nordvik Bank</div>
  <div class="logo-box" style="left:789px">Solvent Partners</div>
  <div class="logo-box" style="left:960px">Relay Telecom</div>
  <div class="arrow" style="left:1129px;top:2197px;background:var(--blue);color:#fff">›</div>

  <!-- TESTIMONIALS -->
  <div class="abs testi"></div>
  <div class="abs serif sec-title" style="top:2390px"><span class="accent">What Client's Say</span> About Lena</div>
  <svg class="spark" style="left:825px;top:2382px" viewBox="0 0 26 22"><path d="M4 2l3 9M14 0l-5 12M24 8l-13 5" stroke="var(--blue)" stroke-width="2" fill="none"/></svg>
  <div class="abs" style="left:0;top:2457px;width:112px;height:183px;background:#fff;opacity:.5"></div>
  <div class="abs" style="left:1088px;top:2457px;width:112px;height:183px;background:#fff;opacity:.5"></div>
  <div class="arrow" style="left:43px;top:2536px;border:1px solid #ccd;color:#889;background:#fff">‹</div>
  <div class="arrow" style="left:1129px;top:2536px;background:var(--blue);color:#fff">›</div>

  <div class="tcard" style="left:142px"><div class="stars">★★★★★</div><p>"When it became apparent that a project would take more time than I had, Lena stepped up to take on the required research. She was thorough and timely; able to meet a last-minute 12-hour deadline. I would highly recommend Lena to assist with your next project."</p></div>
  <div class="tcard" style="left:613px"><div class="stars">★★★★★</div><p>"When it became apparent that a project would take more time than I had, Lena stepped up to take on the required research. She was thorough and timely; able to meet a last-minute 12-hour deadline. I would highly recommend Lena to assist with your next project."</p></div>
  <div class="avatar" style="left:333px;top:2610px" role="img" aria-label="Client photo"></div>
  <div class="avatar" style="left:805px;top:2610px" role="img" aria-label="Client photo"></div>
  <div class="tname" style="left:142px;top:2692px">Dana R.</div>
  <div class="trole" style="left:142px;top:2720px">Owner, Northline Roofing</div>
  <div class="tname" style="left:613px;top:2692px">Dana R.</div>
  <div class="trole" style="left:613px;top:2720px">Owner, Northline Roofing</div>

  <!-- RATES -->
  <div class="abs serif sec-title" style="top:2862px">Rates And Packages <span class="accent">Of Lena Pruvost</span></div>
  <svg class="spark" style="left:830px;top:2852px" viewBox="0 0 26 22"><path d="M4 2l3 9M14 0l-5 12M24 8l-13 5" stroke="#111" stroke-width="2" fill="none"/></svg>
  <div class="rate" style="left:93px"><div class="rate-head" style="background:var(--blue)">Hourly Rate</div><div class="rate-price">$40</div><div class="rate-note">For clients needing only occasional help</div></div>
  <div class="rate" style="left:349px"><div class="rate-head" style="background:var(--green)">20 hours/month</div><div class="rate-price">$700</div><div class="rate-note">Includes one 15 minute meeting per week</div><div class="rate-small">(Responses within 72 hours)</div></div>
  <div class="rate" style="left:606px"><div class="rate-head" style="background:var(--blue)">40 hours/month</div><div class="rate-price">$1,300</div><div class="rate-note">Includes one 30 minute meeting per week</div><div class="rate-small">(Responses within 48 hours)</div></div>
  <div class="rate" style="left:863px"><div class="rate-head" style="background:var(--green)">20 hours/month</div><div class="rate-price">$2,400</div><div class="rate-note">Includes one 60 minute meeting per week</div><div class="rate-small">(Responses within 24 hours)</div></div>
  <div class="btn" style="left:151px;top:3146px;width:127px;height:33px;background:var(--blue)">GET STARTED</div>
  <div class="btn" style="left:407px;top:3146px;width:127px;height:33px;background:var(--green)">GET STARTED</div>
  <div class="btn" style="left:664px;top:3146px;width:127px;height:33px;background:var(--blue)">GET STARTED</div>
  <div class="btn" style="left:921px;top:3146px;width:127px;height:33px;background:var(--green)">GET STARTED</div>

  <!-- CONTACT -->
  <div class="abs contact"></div>
  <div class="abs serif" style="left:138px;top:3394px;font-size:34px"><span class="accent">Get In Touch</span> With Lena Pruvost</div>
  <svg class="spark" style="left:604px;top:3380px" viewBox="0 0 26 22"><path d="M4 2l3 9M14 0l-5 12M24 8l-13 5" stroke="var(--blue)" stroke-width="2" fill="none"/></svg>
  <div class="field" style="left:138px;top:3457px;width:227px">First Name*</div>
  <div class="field" style="left:379px;top:3457px;width:227px">Last Name*</div>
  <div class="field" style="left:138px;top:3508px;width:227px">Phone Number*</div>
  <div class="field" style="left:379px;top:3508px;width:227px">Email*</div>
  <div class="field" style="left:138px;top:3557px;width:468px;height:69px">Message*</div>
  <div class="btn" style="left:138px;top:3656px;width:126px;height:33px;background:var(--blue)">SUBMIT</div>
  <div class="abs laptop" role="img" aria-label="Illustrated avatar waving from a laptop screen"></div>

  <!-- FOOTER -->
  <div class="abs f-title" style="left:91px;top:3836px"><span class="accent">Contact</span> Us</div>
  <div class="f-icon" style="left:93px;top:3885px"><svg width="14" height="14" viewBox="0 0 24 24"><path d="M6 2l4 4-2 3c1 3 4 6 7 7l3-2 4 4-3 4C10 21 3 14 2 5z" fill="#fff"/></svg></div>
  <div class="f-label" style="left:130px;top:3879px"><b>Call Us</b><br>555.014.2290</div>
  <div class="f-icon" style="left:93px;top:3937px"><svg width="14" height="14" viewBox="0 0 24 24" fill="none" stroke="#fff" stroke-width="2.5"><rect x="2" y="5" width="20" height="14"/><path d="M2 5l10 8 10-8"/></svg></div>
  <div class="f-label" style="left:130px;top:3931px"><b>Email</b><br>hello@lenapruvost.example</div>

  <div class="abs" style="left:574px;top:3830px;width:110px;height:102px;border-radius:6px;background:linear-gradient(180deg,#f2c55a,#3aa37a 60%,#8d8d92)" role="img" aria-label="Avatar brand mark"></div>
  <div class="abs" style="left:500px;top:3935px;width:260px;text-align:center;font-family:'PT Serif',serif;font-size:27px;color:#111">Lena Pruvost</div>
  <div class="abs" style="left:500px;top:3970px;width:260px;text-align:center;font-size:11px;font-weight:600;color:var(--blue)">Online Business Manager</div>

  <div class="abs f-title" style="left:985px;top:3836px"><span class="accent">Follow</span> Us On</div>
  <div class="f-icon" style="left:985px;top:3886px"></div>
  <div class="f-label" style="left:1022px;top:3889px">Circlebook</div>
  <div class="f-icon" style="left:985px;top:3935px"></div>
  <div class="f-label" style="left:1022px;top:3938px">ProLink</div>

  <div class="abs" style="left:91px;top:3995px;width:1018px;height:1px;background:var(--line)"></div>
  <div class="abs" style="left:0;top:4027px;width:1200px;text-align:center;font-size:10px;color:#222">© 2023 Lena Pruvost. All Rights Reserved.</div>

</div>
</body>
</html>
```